Truck Driver Pay - Small Infographic

I need a very small, compact infographic to illustrate the differences in pay for a solo truck driver vs. team truck drivers. This illustration will be viewed on the web exclusively. I have sketched out an idea with all of the content that must be included. I just need a designer's touch.

The attached 'mock up' contains the information to be illustrated/communicated by this infographic.

Target Market(s)

Blue collar employee males ages 18-49 with high school education

Requirements
Must have
• I need 2 versions of the graphic:
• 1) 600 pixels wide for desktop presentation
• 2) 300 pixels wide with vertical scroll for mobile.
• I also require the native .psd or .ai files used to create this infographic.

```html
<!DOCTYPE html>
<html lang="en">
<head>
<meta charset="utf-8">
<title>Understanding Driver Pay</title>
<link rel="stylesheet" href="https://fonts.googleapis.com/css2?family=Montserrat:wght@900&family=Jost:wght@300;400;500&family=Noto+Serif:ital,wght@0,400;0,700;1,400;1,700&display=swap">
<style>
:root{
  --header:#2b2b2a;
  --sky:#6dc5d7;
  --grass:#4b6b2c;
  --white:#ffffff;
  --ink:#2e2e2e;
  --gold:#e3c544;
  --title-gold:#ecc93a;
  --panel:#e9e9e6;
  --panel-band:#dfdfdb;
  --panel-light:#f3f3f1;
  --money:#2c7a1a;
  --truck:#cfcfcf;
  --figure:#111111;
}
*{margin:0;padding:0;box-sizing:border-box}
html,body{width:800px;height:1200px;overflow:hidden}
body{position:relative;background:var(--grass);font-family:"Jost",sans-serif;color:var(--white)}
.header{position:absolute;left:0;top:0;width:800px;height:100px;background:var(--header);display:flex;align-items:center;justify-content:center}
.header h1{font-family:"Montserrat",sans-serif;font-weight:900;font-size:47px;letter-spacing:1px;color:var(--white)}
.sky{position:absolute;left:0;top:100px;width:800px;height:230px;background:var(--sky)}
.divider{position:absolute;left:396px;top:100px;height:1100px;border-left:2px dashed var(--white)}
.art{position:absolute}
.truck-art{background:linear-gradient(#dedede,#bdbdbd);border-radius:8px}
.figure-art{background:var(--figure);border-radius:18px 18px 4px 4px}
.label{position:absolute;top:417px;font-size:25px;font-weight:400}
.paycheck{position:absolute;left:37px;top:476px;width:728px;height:287px;background:var(--panel)}
.paycheck-head{height:80px;background:var(--gold);position:relative}
.money-art{position:absolute;left:108px;top:14px;width:96px;height:50px;background:linear-gradient(#7ccf5a,#3e9a2a);border-radius:4px;transform:rotate(-6deg)}
.paycheck-head h2{position:absolute;left:228px;top:16px;font-family:"Noto Serif",serif;font-weight:700;font-size:35px;color:var(--ink)}
.row{position:absolute;left:0;width:728px;color:var(--ink)}
.row-miles{top:82px;height:50px;background:var(--panel-light)}
.row-rate{top:132px;height:50px;background:var(--panel-band)}
.row-pay{top:184px;left:35px;width:658px;height:68px;background:var(--panel-light);border-top:2px solid var(--ink)}
.row .mid{position:absolute;left:0;width:728px;text-align:center;font-weight:500;font-size:21px;top:12px}
.row-pay .mid{left:-35px;top:18px;font-size:24px}
.num{position:absolute;font-family:"Noto Serif",serif;font-style:italic;font-size:26px;top:6px}
.plan{font-size:15px;line-height:14px;display:inline-block;vertical-align:middle;margin-left:4px}
.pay{position:absolute;font-family:"Noto Serif",serif;font-style:italic;font-weight:700;color:var(--money)}
.each{position:absolute;left:515px;top:48px;font-style:italic;font-size:15px}
.footnote{position:absolute;left:35px;top:264px;font-size:11px;color:var(--ink)}
.col{position:absolute;top:800px;width:322px}
.col h3{font-family:"Noto Serif",serif;font-weight:400;font-size:34px;color:var(--title-gold);line-height:48px}
.stripe{width:169px;height:7px;background:var(--title-gold);margin:10px 0 22px}
.col p{font-weight:300;font-size:18.5px;line-height:26px;margin-bottom:20px;text-align:left}
.col-team p{text-align:justify}
</style>
</head>
<body>
<header class="header"><h1>UNDERSTANDING DRIVER PAY</h1></header>
<div class="sky"></div>
<div class="divider"></div>

<div class="art truck-art" style="left:45px;top:150px;width:225px;height:250px" role="img" aria-label="Front view of a box truck labelled SOLO"></div>
<div class="art figure-art" style="left:288px;top:278px;width:48px;height:122px" role="img" aria-label="Silhouette of one driver"></div>
<div class="label" style="left:110px">1 Truck</div>
<div class="label" style="left:263px">1 Driver</div>

<div class="art truck-art" style="left:428px;top:150px;width:225px;height:250px" role="img" aria-label="Front view of a box truck labelled TEAM"></div>
<div class="art figure-art" style="left:670px;top:278px;width:100px;height:122px" role="img" aria-label="Silhouettes of two drivers"></div>
<div class="label" style="left:490px">1 Truck</div>
<div class="label" style="left:660px">2 Drivers</div>

<section class="paycheck">
  <div class="paycheck-head">
    <div class="money-art" role="img" aria-label="Dollar bill icon"></div>
    <h2>Example Pay Check</h2>
  </div>
  <div class="row row-miles">
    <span class="num" style="left:100px">2500</span>
    <span class="mid">Weekly Miles Driven</span>
    <span class="num" style="left:570px">4200</span>
  </div>
  <div class="row row-rate">
    <span class="num" style="left:95px">x .26<span class="plan">classic<br>plan</span></span>
    <span class="mid">Mileage Rate</span>
    <span class="num" style="left:548px">x .175</span>
  </div>
  <div class="row row-pay">
    <span class="pay" style="left:45px;top:6px;font-size:34px">$650</span>
    <span class="mid">Weekly Pay</span>
    <span class="pay" style="left:500px;top:-2px;font-size:42px">$752</span>
    <span class="each">Each Driver</span>
  </div>
  <div class="footnote">*Weekly mileage will vary. For illustration only</div>
</section>

<section class="col col-solo" style="left:44px">
  <h3>Limited Miles</h3>
  <div class="stripe"></div>
  <p>When a solo driver needs to take his required break, the truck has to stop rolling.</p>
  <p>Solo drivers can drive a limited amount of miles due to mandated breaks and rest safty regulations.</p>
</section>

<section class="col col-team" style="left:434px">
  <h3>More Miles</h3>
  <div class="stripe" style="width:272px"></div>
  <p>Team drivers alternate driving duties so the truck cover more miles. When Driver 1 need to take his reqired break, Driver 2 takes over driving duties until his required break and they switch places again.</p>
  <p>The truck keeps rolling and both drives are paid for combined miles the truck has been driven.</p>
</section>
</body>
</html>
```